Fitness Equipment & Service

I want to make the card eye catching and fun. We are called Copperleaf Motion Limited and we are based in Wales. We sell, install and service all types of fitness equipment from Skipping ropes, right through the Dumbbells, Kettle bells and Barbells through to state of the art Treadmills, Running Machines and Strength Equipment. We also design and install changing room furniture and lockers.

TYPOGRAPHY
We would like to use Futrura. Futura has an appearance of efficiency and forwardness. The typeface is derived
from simple geometric forms (near-perfect circles, triangles and squares) and is based on strokes of
near-even weight, which are low in contrast. This is most visible in the almost perfectly round stroke of
the o, which is nonetheless slightly ovoid.
The lowercase has tall ascenders, which rise above the cap line. The uppercase
characters present proportions similar to those of classical Roman capitals.

TYPOGRAPHIC CONSIDERATIONS
No Strike though
No Horizontal Scaling
No Drop Shadows
No Effects
Never use less than 120% Leading

OUR CORPORATE COLOURS
BRAND GUIDELINES
We were thinking that our primary colour palette consists of the Acid Green (Pantone 382) and Process Black.

We work closely with torvane Ltd and would like to include their name on the card somewhere. I have attached images of the other brands that we work with as an idea or the small icons I have included that illustrate what we do?. I have very kindly been given permission to use any of the images off the files that I have included below, so I hope these help. I will include these below. I would be open to suggestions if it made the card more striking Can you do it?

Hi All, Just wanted to add a few thoughts but you are the guys with the creative visions (thats why are here) We are based in Wales, UK and we would be open to lots of different ideas on a theme but must be eye catching, Bold and FUN. If you can or think that the Welsh or any dragon could be put in there then go for it (its not a must have) We have also added some ideas for colour but again its over to you!! GO FOR IT ! Thanks and look forward to your visions! Owen

Hi All, Just thought I would sen through the contact details that need to be on the card. (if you want to play around with icons instead of the wording twitter, Facebook, go for it): Copperleaf Motion Limited Owen Pritchard Managing Director Mob: +44 (0)7391 508 262 e-mail: sales@copperleafmotion.co.uk Web: Copperleafmotion.co.uk twitter: @motionParcelbin Facebook: Copperleaf Motion Limited

```html
<!DOCTYPE html>
<html lang="en">
<head>
<meta charset="utf-8">
<title>Copperleaf Motion Limited – Business Card</title>
<link rel="stylesheet" href="https://fonts.googleapis.com/css2?family=Arimo:wght@400;700&family=Libre+Baskerville:wght@700&display=swap">
<style>
  :root{
    --stage:#e9e7e3;
    --paper:#ffffff;
    --navy:#1f2c78;
    --gold:#c79a3a;
    --ink:#1d1d1f;
    --rule:#3a3a3a;
    --blue-deep:#0f3f86;
    --blue-mid:#1766b8;
    --blue-bright:#1f86d6;
    --blue-sky:#3db5e6;
    --blue-grey:#8fa3b8;
    --blue-night:#0b2e63;
  }
  *{box-sizing:border-box;margin:0;padding:0}
  html,body{width:1200px;height:902px;overflow:hidden;background:var(--stage)}
  body{position:relative;font-family:"Arimo",Arial,sans-serif}

  .card{position:absolute;left:250px;width:700px;height:400px;overflow:hidden;
        box-shadow:0 4px 14px rgba(0,0,0,.18)}
  .card--front{top:40px;background:var(--paper)}
  .card--back{top:462px;background:linear-gradient(135deg,var(--blue-bright),var(--blue-deep))}

  /* front */
  .brand{position:absolute;left:40px;top:60px;width:290px;text-align:center}
  .brand__mark{width:150px;height:150px;border-radius:50%;background:var(--navy);margin:0 auto 20px}
  .brand__name{font-size:22px;font-weight:700;line-height:1.25;color:var(--navy)}
  .divider{position:absolute;left:365px;top:36px;width:2px;height:240px;background:var(--rule)}
  .person{position:absolute;left:395px;top:32px}
  .person__name{font-family:"Libre Baskerville",Georgia,serif;font-weight:700;font-size:30px;line-height:1.2;color:var(--navy)}
  .person__role{font-size:19px;line-height:1.3;color:var(--ink)}
  .contacts{position:absolute;left:395px;top:128px;list-style:none}
  .contacts li{display:flex;align-items:center;gap:12px;font-size:19px;line-height:1.35;color:var(--ink);margin-bottom:4px}
  .contacts .icon{width:16px;height:16px;flex:none;background:var(--navy);display:flex;align-items:center;justify-content:center}
  .wave{position:absolute;left:0;top:0;width:700px;height:400px}
  .email{position:absolute;left:240px;bottom:12px;font-size:20px;line-height:1.2;color:#fff;transform:rotate(-7deg);transform-origin:left bottom;white-space:nowrap}

  /* back */
  .tile{position:absolute;width:110px;height:110px}
  .tile--sky{background:var(--blue-sky)}
  .tile--mid{background:var(--blue-mid)}
  .tile--deep{background:var(--blue-deep)}
  .tile--grey{background:var(--blue-grey)}
  .tile--night{background:var(--blue-night)}
  .back-brand{position:absolute;left:40px;bottom:38px;display:flex;align-items:center;gap:16px}
  .back-brand__mark{width:90px;height:90px;border-radius:50%;background:var(--navy)}
  .back-brand__name{font-size:22px;font-weight:700;line-height:1.25;color:#fff}
</style>
</head>
<body>

<section class="card card--front" aria-label="Card front">
  <div class="brand">
    <div class="brand__mark"></div>
    <p class="brand__name">Copperleaf Motion Limited</p>
  </div>

  <div class="divider"></div>

  <header class="person">
    <h1 class="person__name">Owen Pritchard</h1>
    <p class="person__role">Managing Director</p>
  </header>

  <ul class="contacts">
    <li><span class="icon"><svg width="10" height="10" viewBox="0 0 10 10"><path d="M2 1l2 2-1 1c.6 1.3 1.7 2.4 3 3l1-1 2 2-1.5 1.5C4 9 1 6 .5 2.5z" fill="#fff"/></svg></span>+44 (0)7391 508 262</li>
    <li><span class="icon"></span>@motionParcelbin</li>
    <li><span class="icon"></span>Copperleafmotion.co.uk</li>
    <li><span class="icon"></span>Copperleaf Motion Limited</li>
  </ul>

  <svg class="wave" viewBox="0 0 700 400" aria-hidden="true">
    <path d="M0 400 C180 318 420 278 700 258 L700 400 Z" fill="var(--gold)"/>
    <path d="M0 400 C180 330 420 290 700 270 L700 400 Z" fill="var(--navy)"/>
  </svg>
  <p class="email">sales@copperleafmotion.co.uk</p>
</section>

<section class="card card--back" aria-label="Card back">
  <div class="tile tile--deep" style="left:350px;top:0" role="img" aria-label="Locker icon tile"></div>
  <div class="tile tile--mid" style="left:460px;top:0" role="img" aria-label="Weight bench icon tile"></div>
  <div class="tile tile--deep" style="left:570px;top:0" role="img" aria-label="Skipping rope icon tile"></div>
  <div class="tile tile--mid" style="left:0;top:110px" role="img" aria-label="Treadmill icon tile"></div>
  <div class="tile tile--sky" style="left:110px;top:110px" role="img" aria-label="Exercise bike icon tile"></div>
  <div class="tile tile--mid" style="left:220px;top:110px" role="img" aria-label="Nutrition icon tile"></div>
  <div class="tile tile--night" style="left:330px;top:110px" role="img" aria-label="Dumbbell photograph"></div>
  <div class="tile tile--deep" style="left:440px;top:110px"></div>
  <div class="tile tile--grey" style="left:110px;top:220px;height:70px" role="img" aria-label="Kettlebell icon tile"></div>

  <div class="back-brand">
    <div class="back-brand__mark"></div>
    <p class="back-brand__name">Copperleaf Motion Limited</p>
  </div>
</section>

</body>
</html>
```